Business Card Design

We just need these details on one side of card and logo on the other.

Industry/Entity Type

Business

Contact Information for Business Card

Lisel Pardoe | Artist
118 Coldwell Street
Elmridge North Vic 3162
# 0412 978 205 | 03 9187 2604
lisel@liselpardoe.com
liselsnook.com.au

```html
<!DOCTYPE html>
<html lang="en">
<head>
<meta charset="utf-8">
<title>Lisel's Nook — Business Card</title>
<link href="https://fonts.googleapis.com/css2?family=Questrial&family=Josefin+Sans:wght@400&display=swap" rel="stylesheet">
<style>
  :root {
    --backdrop: #d7d7d7;
    --card: #1f1f1f;
    --ink: #ffffff;
    --accent: #d8262b;
  }
  * { margin: 0; padding: 0; box-sizing: border-box; }
  html, body {
    width: 1200px; height: 999px; overflow: hidden;
    background: var(--backdrop);
    font-family: "Questrial", "Century Gothic", sans-serif;
    color: var(--ink);
  }
  .card {
    position: absolute;
    left: 244px; width: 681px; height: 400px;
    background: var(--card);
    box-shadow: 0 1px 3px rgba(0,0,0,0.35);
  }
  .card--front { top: 102px; }
  .card--back { top: 520px; }

  .brand-name {
    position: absolute; left: 0; right: 0; top: 126px;
    text-align: center;
    font-family: "Questrial", sans-serif;
    font-weight: 400;
    font-size: 94px; line-height: 1; letter-spacing: 1px;
  }
  .brand-tagline {
    position: absolute; left: 0; right: 0; top: 247px;
    display: flex; justify-content: center; align-items: center; gap: 17px;
    font-size: 18px; letter-spacing: 2.4px;
  }
  .brand-tagline .dot {
    width: 6px; height: 6px; border-radius: 50%; background: var(--ink);
  }

  .holder {
    position: absolute; right: 431px; top: 174px; text-align: right;
    font-family: "Josefin Sans", sans-serif;
  }
  .holder-name { font-size: 21px; letter-spacing: 3.6px; line-height: 1; }
  .holder-role { font-size: 18px; letter-spacing: 2.6px; margin-top: 8px; line-height: 1; }

  .divider {
    position: absolute; left: 271px; top: 168px;
    width: 2px; height: 114px; background: var(--accent);
  }

  .contact { position: absolute; left: 298px; top: 172px; font-size: 16px; }
  .contact-row { display: flex; align-items: center; height: 26.3px; white-space: nowrap; }
  .contact-row .icon {
    width: 18px; height: 18px; margin-left: 2px; margin-right: 17px; flex: none;
    display: flex; align-items: center; justify-content: center;
  }
  .contact-row .icon--at { color: var(--accent); font-size: 20px; line-height: 1; }
  .contact-address { letter-spacing: 0.3px; }
  .contact-phone { letter-spacing: 1.2px; word-spacing: 8px; }
  .contact-phone .sep { display: inline-block; width: 2px; height: 14px; background: var(--accent); margin: 0 14px; vertical-align: -2px; }
  .contact-email { letter-spacing: 4.6px; }
  .contact-web { letter-spacing: 6.2px; }
</style>
</head>
<body>
  <section class="card card--front">
    <h1 class="brand-name">Lisel's Nook</h1>
    <p class="brand-tagline">
      <span>STUDIO</span><span class="dot"></span><span>CAFE</span><span class="dot"></span><span>GALLERY</span>
    </p>
  </section>

  <section class="card card--back">
    <div class="holder">
      <p class="holder-name">LISEL PARDOE</p>
      <p class="holder-role">ARTIST</p>
    </div>
    <div class="divider"></div>
    <div class="contact">
      <p class="contact-row contact-address">118 Coldwell Street Elmridge North Vic 3162</p>
      <p class="contact-row contact-phone">
        <svg class="icon" viewBox="0 0 24 24" aria-hidden="true"><path fill="#d8262b" d="M6.6 10.8a15.1 15.1 0 0 0 6.6 6.6l2.2-2.2c.3-.3.7-.4 1-.2 1.1.4 2.3.6 3.6.6.6 0 1 .4 1 1V20c0 .6-.4 1-1 1A17 17 0 0 1 3 4c0-.6.4-1 1-1h3.5c.6 0 1 .4 1 1 0 1.3.2 2.5.6 3.6.1.3 0 .7-.2 1z"/></svg>
        <span>0412 978 205<span class="sep"></span>03 9187 2604</span>
      </p>
      <p class="contact-row contact-email">
        <span class="icon icon--at" aria-hidden="true">@</span>
        <span>lisel@liselpardoe.com</span>
      </p>
      <p class="contact-row contact-web">
        <svg class="icon" viewBox="0 0 24 24" aria-hidden="true"><circle cx="12" cy="12" r="9" fill="none" stroke="#d8262b" stroke-width="2"/><ellipse cx="12" cy="12" rx="4" ry="9" fill="none" stroke="#d8262b" stroke-width="1.6"/><line x1="3" y1="12" x2="21" y2="12" stroke="#d8262b" stroke-width="1.6"/></svg>
        <span>liselsnook.com.au</span>
      </p>
    </div>
  </section>
</body>
</html>
```